Form Crafters Business Card

Professional cosmetic surgery company, based in very exclusive area in London. High profiled clientele. Brand is very artistic, modern, state-of-the-art, safe. The best in the business. Celebrity clientele.

Form Crafter’s of London is a brand serving a discriminating and exclusive clientele who value personal service that is both intimate and high end. Our clients choose Form Crafters because of the relationships we share with all of our customers. The clients of Form Crafters have an equal partnership between customers, and very experienced, highly qualified medical professionals. This together provides you with a professional service that keeps you looking good and feeling good. It is a relationship based on honesty, compassion, loyalty and respect.
Form Crafter’s have provided services for internationally recognised celebrities, and other high profiled individuals.

The cards are used for networking at private, exclusive events with VIPs.

Target Market(s)

Professionals
Rich people

Industry/Entity Type

Professional Service

Contact Information for Business Card

Need double sided business card design for 4 people. Back of the business card needs to have contrast background to the front with butterfly watermark with services provided:
Hair Restoration surgery
Hair Loss treatments
Breast surgery
Rhinoplasty
Sonix Liposuction
Fat Grafting
Relaxin & Fillers

Front of the business card needs to be a nice satin black.
with following information:
Tavish Kolendran - name
Chief Executive - Job title

www.formcrafters.co.uk
tavish@formcrafters.co.uk
Phone: +44 (0)207 461 2295
Mobile: +44 (0)7912 548 237

The London Ashcombe Clinic
14 Ashcombe Street | London | W1K 3PQ
Off Tolland Street

All business cards have the same address, phone, website as Tavish's details.
Same details on the back of the business card as well.
The other cards have different name, job title, email, mobile number

Faraz Qureshi - Name
Partner - Job Title
Former England International Cricketer - please include below job title

email: faraz@formcrafters.co.uk
mobile: +44(0)7846 205318

Dr Tadeu Varella - Name
Plastic Surgeon - Job Title
drvarella@formcrafters.co.uk
No mobile number

Dr Zain Hussaini FRCS (please put FRCS in small font) - Name
Hair Restoration Surgeon - Job Title
drhussaini@formcrafters.co.uk
No mobile number

Colors
cedeec
85abd2
0655a3

Requirements
Must have
• The logo needs to be in a metallic finish
• Text needs to be striking
• nice background
• butterfly watermark on the back

```html
<!DOCTYPE html>
<html lang="en">
<head>
<meta charset="utf-8">
<title>Form Crafters Business Card</title>
<link rel="stylesheet" href="https://fonts.googleapis.com/css2?family=Poiret+One&family=Source+Sans+3:wght@400;600&display=swap">
<style>
  :root {
    --stage-light: #f4f4f4;
    --stage-dark: #cfcfcf;
    --card-white: #ffffff;
    --card-black: #050505;
    --brand-blue: #1a7fc9;
    --brand-blue-deep: #0655a3;
    --brand-orange: #f08a1c;
    --divider: #9a9a9a;
    --caption: #6b6b6b;
  }
  * { margin: 0; padding: 0; box-sizing: border-box; }
  html, body { width: 1200px; height: 960px; overflow: hidden; }
  body {
    position: relative;
    background: radial-gradient(circle at 60% 35%, var(--stage-light) 0%, var(--stage-dark) 100%);
    font-family: "Source Sans 3", "Myriad Pro", sans-serif;
  }

  .card {
    position: absolute;
    width: 520px;
    height: 300px;
    box-shadow: 0 10px 24px rgba(0,0,0,0.22);
  }

  /* Services side */
  .card--services {
    left: 110px;
    top: 100px;
    background: var(--card-white);
    display: flex;
    align-items: center;
  }
  .services__mark {
    width: 200px;
    display: flex;
    justify-content: center;
    align-items: center;
  }
  .services__divider {
    width: 1px;
    height: 140px;
    background: var(--divider);
  }
  .services__body { padding-left: 40px; }
  .brand-name {
    font-family: "Poiret One", "Josefin Sans", sans-serif;
    color: var(--brand-blue);
    font-size: 24px;
    letter-spacing: 0.5px;
    font-variant: small-caps;
    margin-bottom: 10px;
  }
  .services__list {
    list-style: none;
    color: var(--brand-blue);
    font-size: 13.5px;
    line-height: 16px;
  }

  /* Contact side */
  .card--contact {
    left: 570px;
    top: 560px;
    background: var(--card-black);
    text-align: center;
    padding-top: 70px;
  }
  .card--contact .brand-name { font-size: 22px; margin-bottom: 6px; }
  .contact__details {
    color: var(--brand-blue);
    font-size: 12.5px;
    line-height: 15px;
  }
  .contact__address {
    margin-top: 26px;
    color: var(--brand-orange);
    font-size: 9.5px;
    line-height: 12px;
  }

  /* Standalone mark */
  .mark-large {
    position: absolute;
    left: 110px;
    top: 640px;
    width: 330px;
    display: flex;
    align-items: center;
    gap: 14px;
  }
  .mark-large .brand-name { font-size: 40px; margin: 0; }
  .mark-dot {
    width: 22px; height: 22px; border-radius: 50%;
    background: var(--brand-blue-deep);
  }
  .caption {
    position: absolute;
    left: 85px;
    top: 838px;
    font-size: 32px;
    color: var(--caption);
    letter-spacing: 0.5px;
  }
</style>
</head>
<body>

  <section class="card card--services">
    <div class="services__mark">
      <svg width="26" height="26" viewBox="0 0 26 26" aria-hidden="true">
        <circle cx="13" cy="13" r="12" fill="var(--brand-blue-deep)"/>
      </svg>
    </div>
    <div class="services__divider"></div>
    <div class="services__body">
      <p class="brand-name">Form Crafters</p>
      <ul class="services__list">
        <li>Hair Restoration surgery</li>
        <li>Hair Loss treatments</li>
        <li>Breast surgery</li>
        <li>Rhinoplasty Sonix Liposuction</li>
        <li>Fat Grafting Relaxin &amp; Fillers</li>
      </ul>
    </div>
  </section>

  <section class="card card--contact">
    <p class="brand-name">Form Crafters</p>
    <div class="contact__details">
      <p>Tavish Kolendran</p>
      <p>Chief Executive</p>
      <p>www.formcrafters.co.uk</p>
      <p>tavish@formcrafters.co.uk</p>
      <p>Phone: +44 (0)207 461 2295</p>
      <p>Mobile: +44 (0)7912 548 237</p>
    </div>
    <div class="contact__address">
      <p>The London Ashcombe Clinic</p>
      <p>14 Ashcombe Street</p>
      <p>W1K 3PQ Off Tolland Street</p>
      <p>London</p>
    </div>
  </section>

  <div class="mark-large">
    <span class="mark-dot"></span>
    <p class="brand-name">Form Crafters</p>
  </div>

  <p class="caption">BUSINESS CARD DESIGN</p>

</body>
</html>
```